Fox Lantern Brewing Company Spring 2024

https://www.foxlanternportal.example/
www.FoxlanternBrewing.example
Spring Menu change for Brewery, focus on menu that is upmarket yet fresh and fun. 11"x18" layout both sides. out brand kit online offers a lot of direction with fonts, colors, and logos. We do two menu changes a year and want to keep that same look once we find a great design.
Target Market(s)
30-60 year old
Industry/Entity Type
Brewery Restaurant
Font styles to use
Other font styles liked:
- See Brand Kit
Colors
00AB8E
00BBA5
67D7C9
C6EFE9
E9F9F6
Requirements
Must have
- Menu engineering
Nice to have
- Stock food photos

```html
<!DOCTYPE html>
<html lang="en">
<head>
<meta charset="utf-8">
<title>Fox Lantern Brewing Company — Spring Menu</title>
<link href="https://fonts.googleapis.com/css2?family=Alfa+Slab+One&family=Work+Sans:wght@500;600&family=Crimson+Text&family=Yellowtail&display=swap" rel="stylesheet">
<style>
  :root{
    --ink:#1f3d33;
    --gold:#b48f3c;
    --paper:#f8f4ea;
    --backdrop:#0f2a24;
  }
  *{box-sizing:border-box;margin:0;padding:0}
  html,body{width:1200px;height:791px;overflow:hidden;background:var(--backdrop)}
  .menu{position:absolute;left:365px;top:10px;width:470px;height:770px;background:var(--paper);color:var(--ink);font-family:"Work Sans",sans-serif}
  .brand{position:absolute;left:30px;top:48px;width:180px;text-align:center;font-family:"Alfa Slab One",serif;color:var(--ink);line-height:1.05}
  .brand-dot{width:34px;height:34px;border-radius:50%;background:var(--ink);margin:0 auto 10px}
  .brand-name{font-size:19px;letter-spacing:1.5px}
  .brand-sub{font-size:13px;letter-spacing:2px;margin-top:4px}
  .panel{position:absolute;border:1px solid var(--gold);display:flex;flex-direction:column}
  .panel-apps{left:22px;top:219px;width:206px;height:512px;padding:0 7px 0 8px}
  .panel-right{left:243px;top:40px;width:206px;height:690px}
  .section-title{font-family:"Alfa Slab One",serif;font-size:17px;letter-spacing:1.5px;text-align:center}
  .apps-title{height:35px;line-height:38px}
  .salads-title{height:33px;line-height:36px}
  .table{border-left:1px solid var(--ink);border-top:1px solid var(--ink);border-bottom:1px solid var(--ink);display:flex;flex-direction:column}
  .row{position:relative;border-bottom:1px solid var(--ink);padding:6px 30px 0 9px;flex:1}
  .row:last-child{border-bottom:none}
  .row.col::after{content:"";position:absolute;right:47px;top:0;bottom:0;border-left:1px solid var(--ink)}
  .name{font-size:7.2px;font-weight:600;letter-spacing:1.2px;text-transform:uppercase}
  .tag{color:var(--gold)}
  .mark{display:inline-block;width:5px;height:5px;border-radius:50%;background:var(--gold);margin-left:3px;vertical-align:1px}
  .desc{font-family:"Crimson Text",serif;font-size:5.3px;line-height:1.25;margin-top:1px}
  .price{position:absolute;right:6px;top:6px;font-size:6.6px;letter-spacing:1px;width:38px;text-align:center}
  .chips{height:150px;flex:none;padding:6px 0 0 9px;position:relative}
  .chips::after{content:"";position:absolute;right:47px;top:0;bottom:0;border-left:1px solid var(--ink)}
  .chips .group{font-size:7px;letter-spacing:1.2px;font-weight:600;margin-bottom:8px}
  .sub{position:relative;padding:0 60px 0 18px;margin-bottom:7px}
  .sub .price{top:0;right:4px}
  .apps-table{height:382px}
  .apps-table .row{padding-right:55px}
  .apps-table .row .price{right:4px}
  .wings{border:1px solid var(--gold);margin-top:5px;height:45px;padding:4px 4px}
  .wings .counts{font-size:6.6px;letter-spacing:1px;text-align:center;margin-top:5px}
  .addons{display:flex;align-items:center;flex:1}
  .script{font-family:"Yellowtail",cursive;font-size:12px;width:50px;padding-left:3px;border-right:1px solid var(--gold);line-height:20px;margin-right:8px}
  .addon-list{flex:1;text-align:center;font-size:6.4px;letter-spacing:1.3px;font-weight:600;line-height:1.8}
  .salads-table{height:180px;margin-left:8px;border-right:1px solid var(--ink)}
  .salads-table .row{padding-right:52px}
  .salads-addons{height:40px;padding:0 8px 0 8px;border-bottom:1px solid var(--gold)}
  .burgers-head{height:60px;text-align:center;padding-top:6px}
  .burgers-head .section-title{line-height:22px}
  .rule{width:40px;height:1px;background:var(--gold);margin:3px auto 3px;position:relative}
  .rule::after{content:"";position:absolute;left:17px;top:-2px;width:5px;height:5px;border-radius:50%;background:var(--gold)}
  .burgers-head .note{font-family:"Crimson Text",serif;font-size:5.2px;padding:0 24px;line-height:1.3}
  .burgers-table{height:309px;margin-left:8px;margin-right:7px;border-right:1px solid var(--ink)}
  .burgers-table .row{padding-right:48px}
  .burgers-addons{height:33px;padding:0 8px}
  .fries-swap{height:35px;padding:0 8px}
</style>
</head>
<body>
<main class="menu">
  <header class="brand" aria-label="Fox Lantern Brewing Company">
    <div class="brand-dot"></div>
    <div class="brand-name">FOX LANTERN</div>
    <div class="brand-name">BREWING</div>
    <div class="brand-sub">COMPANY</div>
  </header>

  <section class="panel panel-apps">
    <h2 class="section-title apps-title">APPETIZERS</h2>
    <div class="table apps-table">
      <div class="chips">
        <div class="group">CHIPS AND ...</div>
        <div class="sub"><div class="name">The Trio</div><div class="desc">A half-size serving each of the Fox Lantern Blonde Beer Cheese, Guacamole, and Salsa.</div><span class="price">14</span></div>
        <div class="sub"><div class="name">Guacamole <span class="tag">(V)</span></div><span class="price">6.5 / 11</span></div>
        <div class="sub"><div class="name">Salsa <span class="tag">(V)</span></div><span class="price">6 / 9.5</span></div>
        <div class="sub"><div class="name">Fox Lantern Blonde<br>Beer Cheese</div><span class="price">6.5 / 11.5</span></div>
        <div class="sub"><div class="name">Grizzly Queso<span class="mark"></span></div><div class="desc">Fox Lantern Beer Cheese topped with a scoop of guac, pico de gallo, and cotija cheese.</div><span class="price">7 / 11.5</span></div>
      </div>
      <div class="row" style="border-top:1px solid var(--ink)"><div class="name">Truffle Fries <span class="tag">(V)</span></div><div class="desc">Truffle salted, frenchly fried potatoes. Served with truffle aioli, garnished with shredded Asiago.</div><span class="price">8</span></div>
      <div class="row"><div class="name">Truffle Sprouts <span class="tag">(V)</span></div><div class="desc">Fresh fried brussel sprouts topped with our truffle aioli, pecans and Asiago cheese.</div><span class="price">11.5</span></div>
      <div class="row"><div class="name">Onion Rings</div><div class="desc">Beer battered onion rings served with a house made Lantern sauce.</div><span class="price">8.5</span></div>
      <div class="row"><div class="name">Texas Poutine<span class="mark"></span></div><div class="desc">French fries topped with ancho cheddar gravy, chopped brisket, pico de gallo.</div><span class="price">10</span></div>
      <div class="row"><div class="name">Cheese Curds</div><div class="desc">Crispy fried cheesey goodness. Served with a zesty chipotle-lime sauce.</div><span class="price">9.5</span></div>
      <div class="row"><div class="name">Embellished Nachos</div><div class="desc">Corn tortilla chips with Fox Lantern Blonde Beer Cheese, refried beans, cotija cheese, lettuce, pico de gallo, pickled onions, jalapeños and sour cream.</div><span class="price">11.5</span></div>
    </div>
    <div class="wings">
      <div class="name">Chicken Wings</div>
      <div class="desc">Chicken wings hand tossed in your choice of sauce. Served with celery and ranch or blue cheese.</div>
      <div class="counts">6 for 10.5 &nbsp;·&nbsp; 12 for 16 &nbsp;·&nbsp; 18 for 22</div>
    </div>
    <div class="addons"><span class="script">Add Ons</span><div class="addon-list">BRISKET 4 · PORK BELLY 3<br>ASADA 3 · CHICKEN 3</div></div>
  </section>

  <section class="panel panel-right">
    <h2 class="section-title salads-title">SALADS</h2>
    <div class="table salads-table">
      <div class="row col"><div class="name">Wedge Salad</div><div class="desc">Iceberg lettuce with bacon crumbles, tomatoes, blue cheese crumbles, and blue cheese dressing.</div><span class="price">6 / 11</span></div>
      <div class="row col"><div class="name">The Seasonal One <span class="tag">(GF) (V)</span></div><div class="desc">Spring mixed greens, strawberries, goat cheese, red onions, and toasted pecans. Served with honey-balsamic dressing.</div><span class="price">6 / 11</span></div>
      <div class="row col"><div class="name">The Champ <span class="tag">(V)</span></div><div class="desc">Spring mix with tomato, avocado, cucumber, and red onion. Served with jalapeño cilantro dressing and topped with crisp tortilla strips.</div><span class="price">6 / 11</span></div>
      <div class="row col"><div class="name">El Oso <span class="tag">(GF) (V)</span><span class="mark"></span></div><div class="desc">Romaine lettuce with grilled corn, black beans, tomatoes, red onion, bell peppers, and chipotle-lime dressing. Topped with Cotija cheese.</div><span class="price">6 / 11</span></div>
    </div>
    <div class="addons salads-addons"><span class="script">Add Ons</span><div class="addon-list">FAJITA CHICKEN 2 / 4<br>POACHED SHRIMP 3 / 5</div></div>

    <div class="burgers-head">
      <h2 class="section-title">BURGERS</h2>
      <div class="rule"></div>
      <p class="note">All beef patties are cooked medium well and served on a toasted bun with fries or a side of greens, pickles and sauce.</p>
    </div>
    <div class="table burgers-table">
      <div class="row col"><div class="name">The Classic One</div><div class="desc">8 oz. Hollow Creek patty with lettuce, tomato, onion, and home-made pickles.</div><span class="price">12.5</span></div>
      <div class="row"><div class="name">Eggsillent Guy</div><div class="desc">Breakfast burger with bacon, cheddar, a fried egg, and Lantern sauce.</div><span class="price">15.25</span></div>
      <div class="row"><div class="name">The Farmer's Cut</div><div class="desc">8 oz. Hollow Creek patty with jack cheese, thick cut bacon, grilled mushrooms, and white truffle aioli.</div><span class="price">14.75</span></div>
      <div class="row"><div class="name">The Legendary One</div><div class="desc">8 oz. Hollow Creek patty with thick cut bacon, caramelized onions, aged cheddar, and roasted garlic aioli.</div><span class="price">14.75</span></div>
      <div class="row"><div class="name">The Laredo One</div><div class="desc">Jack cheese, pico de gallo, mashed avocado, pickled jalapeños with chipotle aioli.</div><span class="price">15.5</span></div>
      <div class="row"><div class="name">The Lubbock</div><div class="desc">Bacon, cheddar cheese, onion rings, BBQ sauce.</div><span class="price">15.5</span></div>
      <div class="row"><div class="name">El Dorado</div><div class="desc">Half-pound burger with pork belly, cheddar cheese, and horseradish mustard aioli.</div><span class="price">16</span></div>
      <div class="row"><div class="name">Royale with Cheese</div><div class="desc">Served on Texas toast with caramelized onions, cheddar cheese, and Monterey Jack cheese with Lantern sauce.</div><span class="price">14.5</span></div>
    </div>
    <div class="addons burgers-addons"><span class="script">Add Ons</span><div class="addon-list">CHEESE 1 · JALAPEÑOS 1<br>BACON 2</div></div>
    <div class="addons fries-swap"><span class="script">Sub Fries</span><div class="addon-list">PICK ANY OF OUR SALADS 2<br>TRUFFLE FRIES 2</div></div>
  </section>
</main>
</body>
</html>
```